Redesign Colorful Business Card

Please redesign the card attached. It is too busy. Please don't eliminate any of the words. The repetivite word "free" can be used less often.

Target Market(s)

College Students.

Contact Information for Business Card

The details listed in the attached image

Font styles to use
Sans Serif

Requirements
Must have
• A clear and simple presentation and must be attractive.

```html
<!DOCTYPE html>
<html lang="en">
<head>
<meta charset="utf-8">
<title>StudyNimbl Business Card</title>
<link rel="stylesheet" href="https://fonts.googleapis.com/css2?family=Poppins:wght@500;600;700&display=swap">
<style>
  :root {
    --page-bg: #f1f1f1;
    --ink-dark: #262626;
    --paper-white: #ffffff;
    --turquoise: #00d2c8;
    --magenta: #f21ee0;
    --slate: #4a4a4a;
    --badge-grey-text: #555555;
  }
  html, body {
    margin: 0;
    width: 1200px;
    height: 1200px;
    overflow: hidden;
    background: var(--page-bg);
  }
  .presentation {
    width: 1200px;
    height: 1200px;
    display: flex;
    flex-direction: column;
    align-items: center;
    justify-content: center;
    gap: 80px;
  }
  .card {
    position: relative;
    width: 33.6em;
    height: 20em;
    background: var(--ink-dark);
    overflow: hidden;
    font-family: "Poppins", sans-serif;
    box-shadow: 0 0.4em 1.2em rgba(0,0,0,0.12);
  }
  .card--colour { font-size: 25px; --accent-bg: var(--turquoise); --mid-line: var(--magenta); --badge-fill: var(--magenta); --badge-text: var(--paper-white); }
  .card--mono { font-size: 16.667px; --accent-bg: var(--slate); --mid-line: var(--paper-white); --badge-fill: var(--paper-white); --badge-text: var(--badge-grey-text); }

  .card__accent {
    position: absolute;
    top: 0; right: 0; bottom: 0;
    left: 16.8em;
    background: var(--accent-bg);
  }
  .card__mascot-area {
    position: absolute;
    left: 0; bottom: 0;
    top: 2.6em;
    width: 16.8em;
    background: var(--paper-white);
    border-top-right-radius: 3em;
  }
  .brand {
    position: absolute;
    left: 1.6em;
    top: 10.2em;
    display: flex;
    align-items: center;
    gap: 0.45em;
  }
  .brand__mark {
    width: 1.1em;
    height: 1.1em;
    background: var(--ink-dark);
  }
  .brand__name {
    font-weight: 500;
    font-size: 1.3em;
    color: var(--ink-dark);
    letter-spacing: -0.01em;
  }
  .badge {
    position: absolute;
    right: 1.9em;
    top: 1.1em;
    width: 4.6em;
    height: 4.6em;
  }
  .badge svg { width: 100%; height: 100%; display: block; }
  .badge__star { fill: var(--badge-fill); }
  .badge__label {
    position: absolute;
    inset: 0;
    display: flex;
    align-items: center;
    justify-content: center;
    font-weight: 700;
    font-size: 1.05em;
    color: var(--badge-text);
    transform: rotate(20deg);
    letter-spacing: 0.03em;
  }
  .benefits {
    position: absolute;
    left: 18.6em;
    top: 5.6em;
    margin: 0;
    padding: 0;
    list-style: none;
  }
  .benefits__item {
    font-weight: 600;
    font-size: 0.66em;
    line-height: 1.3;
    text-transform: uppercase;
    color: var(--paper-white);
    margin-bottom: 1.3em;
  }
  .benefits__item--highlight { color: var(--mid-line); }
</style>
</head>
<body>
  <main class="presentation">
    <article class="card card--colour">
      <div class="card__accent"></div>
      <div class="card__mascot-area" role="img" aria-label="White elephant silhouette illustration"></div>
      <div class="brand">
        <span class="brand__mark"></span>
        <span class="brand__name">StudyNimbl</span>
      </div>
      <div class="badge">
        <svg viewBox="0 0 100 100" aria-hidden="true">
          <polygon class="badge__star" points="100,50 89.6,60.6 93.3,75 79,79 75,93.3 60.6,89.6 50,100 39.4,89.6 25,93.3 21,79 6.7,75 10.4,60.6 0,50 10.4,39.4 6.7,25 21,21 25,6.7 39.4,10.4 50,0 60.6,10.4 75,6.7 79,21 93.3,25 89.6,39.4"/>
        </svg>
        <span class="badge__label">FREE</span>
      </div>
      <ul class="benefits">
        <li class="benefits__item">Cut study time<br>down by up to 50%</li>
        <li class="benefits__item benefits__item--highlight">Learn a subject without<br>having to go to class</li>
        <li class="benefits__item">Memorize anything<br>quickly</li>
      </ul>
    </article>

    <article class="card card--mono">
      <div class="card__accent"></div>
      <div class="card__mascot-area" role="img" aria-label="White elephant silhouette illustration"></div>
      <div class="brand">
        <span class="brand__mark"></span>
        <span class="brand__name">StudyNimbl</span>
      </div>
      <div class="badge">
        <svg viewBox="0 0 100 100" aria-hidden="true">
          <polygon class="badge__star" points="100,50 89.6,60.6 93.3,75 79,79 75,93.3 60.6,89.6 50,100 39.4,89.6 25,93.3 21,79 6.7,75 10.4,60.6 0,50 10.4,39.4 6.7,25 21,21 25,6.7 39.4,10.4 50,0 60.6,10.4 75,6.7 79,21 93.3,25 89.6,39.4"/>
        </svg>
        <span class="badge__label">FREE</span>
      </div>
      <ul class="benefits">
        <li class="benefits__item">Cut study time<br>down by up to 50%</li>
        <li class="benefits__item benefits__item--highlight">Learn a subject without<br>having to go to class</li>
        <li class="benefits__item">Memorize anything<br>quickly</li>
      </ul>
    </article>
  </main>
</body>
</html>
```